Pemberton Dialworks Business Card Design

Double Sided Business Card Design for a Locksmith company specializing in Safecracking, safe & vault service.

```html
<!DOCTYPE html>
<html lang="en">
<head>
<meta charset="utf-8">
<title>Pemberton Dialworks – Business Card</title>
<link href="https://fonts.googleapis.com/css2?family=Lato:wght@300;400;700;900&display=swap" rel="stylesheet">
<style>
  :root {
    --green: #367c3d;
    --green-light: #5fae62;
    --ink: #1d1d1d;
    --heading: #2f2f2f;
    --muted: #a6a6a6;
    --paper: #ffffff;
    --pattern: #f6f6f6;
    --decor: #eeeeee;
  }
  * { box-sizing: border-box; margin: 0; padding: 0; }
  html, body { width: 1010px; height: 1200px; overflow: hidden; background: var(--paper); }
  body { position: relative; font-family: 'Lato', sans-serif; }

  .card {
    position: absolute;
    background: var(--paper);
    overflow: hidden;
    outline: 1px solid #e4e4e4;
  }

  /* Front */
  .card--front { left: 141px; top: 223px; width: 553px; height: 358px; }
  .front-pattern {
    position: absolute; left: 9px; top: 9px; right: 9px; bottom: 9px;
    background: var(--pattern);
    border-radius: 4px;
  }
  .front-brand {
    position: absolute; left: 96px; top: 121px;
    display: flex; align-items: center; gap: 18px;
  }
  .brand-dot {
    width: 100px; height: 100px; border-radius: 50%;
    background: var(--green);
  }
  .front-brand .brand-name {
    font-weight: 900; font-size: 34px; line-height: 1.05;
    color: var(--green); text-transform: uppercase; letter-spacing: 0.5px;
  }

  /* Back */
  .card--back { left: 315px; top: 618px; width: 555px; height: 360px; }
  .back-decor { position: absolute; left: 0; top: 0; }
  .back-brand {
    position: absolute; left: 37px; top: 27px;
    display: flex; align-items: center; gap: 10px;
  }
  .back-brand .brand-dot { width: 52px; height: 52px; }
  .back-brand .brand-name {
    font-weight: 900; font-size: 17px; line-height: 1.05;
    color: var(--green); text-transform: uppercase; letter-spacing: 0.3px;
  }

  .features { position: absolute; left: 281px; top: 30px; width: 260px; }
  .feature { position: absolute; left: 0; display: flex; gap: 7px; }
  .feature--satisfaction { top: 0; }
  .feature--damage { top: 91px; }
  .feature--experience { top: 168px; }
  .feature-icon { flex: 0 0 37px; width: 37px; height: 37px; }
  .feature-title {
    font-size: 19px; font-weight: 400; color: var(--heading);
    line-height: 1.1; margin-top: 9px; white-space: nowrap;
  }
  .feature-text {
    font-size: 13.5px; font-weight: 300; color: var(--muted);
    line-height: 17px; margin-top: 4px;
  }

  .cta-band {
    position: absolute; left: 0; top: 281px; width: 100%; height: 48px;
    background: var(--green); color: #fff;
    display: flex; align-items: center; justify-content: center;
    font-size: 23px; font-weight: 400;
  }
  .cta-band strong { font-weight: 700; margin-left: 6px; }
</style>
</head>
<body>

<section class="card card--front" aria-label="Card front">
  <div class="front-pattern" role="img" aria-label="Faint repeating pattern of safe combination dials"></div>
  <div class="front-brand">
    <span class="brand-dot"></span>
    <div class="brand-name">Pemberton<br>Dialworks</div>
  </div>
</section>

<section class="card card--back" aria-label="Card back">
  <svg class="back-decor" width="555" height="360" viewBox="0 0 555 360" role="img" aria-label="Faint city skyline and safe dial illustration">
    <circle cx="86" cy="178" r="172" fill="var(--decor)"/>
  </svg>

  <div class="back-brand">
    <span class="brand-dot"></span>
    <div class="brand-name">Pemberton<br>Dialworks</div>
  </div>

  <div class="features">
    <div class="feature feature--satisfaction">
      <svg class="feature-icon" viewBox="0 0 37 37" aria-hidden="true">
        <path d="M1 36 V18 A17 17 0 1 1 18 36 Z" fill="none" stroke="var(--green-light)" stroke-width="1.2"/>
        <rect x="11" y="14" width="15" height="9" rx="2" fill="none" stroke="var(--green-light)" stroke-width="1.2"/>
        <path d="M15 21 L22 16" stroke="var(--green-light)" stroke-width="1.2"/>
      </svg>
      <div>
        <h3 class="feature-title">Satisfaction Guaranteed</h3>
        <p class="feature-text">You don't pay unless we open<br>your container</p>
      </div>
    </div>

    <div class="feature feature--damage">
      <svg class="feature-icon" viewBox="0 0 37 37" aria-hidden="true">
        <path d="M1 36 V18 A17 17 0 1 1 18 36 Z" fill="none" stroke="var(--green-light)" stroke-width="1.2"/>
        <circle cx="18" cy="20" r="6" fill="none" stroke="var(--green-light)" stroke-width="1.2"/>
        <path d="M18 20 L21 17 M17 12 H20" stroke="var(--green-light)" stroke-width="1.2"/>
      </svg>
      <div>
        <h3 class="feature-title">No Damage</h3>
        <p class="feature-text">We never damage containers</p>
      </div>
    </div>

    <div class="feature feature--experience">
      <svg class="feature-icon" viewBox="0 0 37 37" aria-hidden="true">
        <path d="M1 36 V18 A17 17 0 1 1 18 36 Z" fill="none" stroke="var(--green-light)" stroke-width="1.2"/>
        <path d="M12 21 V18 A6 6 0 0 1 24 18 V21" fill="none" stroke="var(--green-light)" stroke-width="1.2"/>
        <rect x="11" y="19" width="3" height="5" rx="1" fill="var(--green-light)"/>
        <rect x="22" y="19" width="3" height="5" rx="1" fill="var(--green-light)"/>
      </svg>
      <div>
        <h3 class="feature-title">Customer Experience</h3>
        <p class="feature-text">We value our clients, and you will<br>feel that throughout the process</p>
      </div>
    </div>
  </div>

  <div class="cta-band">Call now for free estimate! <strong>555-014-0192</strong></div>
</section>

</body>
</html>
```